Looking for a modern, Professional business card design

We have a simple business card, but are looking for a more modern, professional look. A sample of the basic card is attached as well as the logo. We would also like to add that we offer:
Struggling with your finances?
- Learn to become debt free
- Discover the power of cash
- Control your money instead of it controlling you
Let us help you achieve a new level of financial freedom!
Also, we would like to have a "SPECIAL OFFER!: FREE 30 minute consultation"
Financial Planning

```html
<!DOCTYPE html>
<html lang="en">
<head>
<meta charset="utf-8">
<title>Clearpath Money Coaching – Business Card</title>
<link rel="stylesheet" href="https://fonts.googleapis.com/css2?family=Lato:wght@300;400;700;900&display=swap">
<style>
  :root {
    --bg: #f3f4ef;
    --card-white: #ffffff;
    --band-dark: #6a7d50;
    --panel-olive: #a8b262;
    --rule-olive: #8e9a4e;
    --ink: #1c1f14;
    --ink-green: #2f3d1c;
    --pale-title: #f4f6dc;
    --brand-dark: #1e1612;
    --brand-green: #7d9448;
  }
  * { margin: 0; padding: 0; box-sizing: border-box; }
  html, body { width: 997px; height: 1200px; overflow: hidden; }
  body { background: var(--bg); font-family: "Lato", sans-serif; color: var(--ink); position: relative; }

  .card {
    position: absolute; left: 192px; width: 640px; height: 384px;
    background: var(--card-white);
    box-shadow: 0 10px 40px rgba(90, 110, 70, 0.25);
    overflow: hidden;
  }
  .card--front { top: 168px; }
  .card--back { top: 663px; }

  .front__band { position: absolute; left: 0; top: 0; width: 43px; height: 100%; background: var(--band-dark); }
  .front__panel { position: absolute; left: 343px; top: 0; width: 297px; height: 100%; background: var(--panel-olive); }

  .brand { position: absolute; display: flex; align-items: center; gap: 10px; }
  .brand__dot { width: 22px; height: 22px; border-radius: 50%; background: var(--brand-green); flex: none; }
  .brand__name { font-weight: 900; color: var(--brand-dark); line-height: 1.05; font-size: 24px; letter-spacing: 0.5px; }
  .card--front .brand { left: 80px; top: 108px; }
  .card--back .brand { left: 0; right: 0; top: 78px; justify-content: center; }

  .offer { position: absolute; right: 326px; top: 254px; text-align: right; color: var(--ink-green); font-size: 16px; line-height: 1.25; }
  .offer__title { font-weight: 700; }
  .offer strong { font-weight: 700; }

  .person { position: absolute; left: 375px; top: 56px; }
  .person__name { font-size: 23px; font-weight: 400; color: var(--ink); letter-spacing: 0.2px; }
  .person__name b { font-weight: 900; }
  .person__role { font-size: 13.5px; color: var(--pale-title); font-weight: 400; margin-top: 1px; }

  .rule { position: absolute; left: 343px; width: 297px; height: 1px; background: var(--rule-olive); }

  .contact { position: absolute; left: 356px; display: flex; align-items: center; gap: 9px; font-size: 15.5px; color: var(--ink); }
  .contact svg { width: 17px; height: 17px; flex: none; }

  .pitch { position: absolute; left: 0; right: 0; top: 175px; text-align: center; color: var(--ink-green); font-size: 15.5px; line-height: 1.22; }
  .pitch__lead { font-weight: 700; margin-bottom: 14px; }
  .pitch__close { font-weight: 700; margin-top: 14px; }
  .pitch b { font-weight: 700; }

  .back__band { position: absolute; left: 0; bottom: 0; width: 100%; height: 44px; background: var(--band-dark); }
</style>
</head>
<body>

<section class="card card--front">
  <div class="front__band"></div>
  <div class="brand">
    <span class="brand__dot"></span>
    <span class="brand__name">CLEARPATH<br>MONEY COACHING</span>
  </div>
  <p class="offer">
    <span class="offer__title">SPECIAL OFFER</span><br>
    <strong>FREE</strong> 30 minute consultation
  </p>

  <div class="front__panel"></div>
  <div class="person">
    <p class="person__name"><b>DANIEL R.</b> HALE</p>
    <p class="person__role">PERSONAL FINANCIAL COACH</p>
  </div>
  <div class="rule" style="top:103px"></div>
  <div class="rule" style="top:151px"></div>
  <div class="rule" style="top:199px"></div>
  <div class="rule" style="top:215px"></div>
  <div class="rule" style="top:263px"></div>
  <div class="rule" style="top:279px"></div>
  <div class="rule" style="top:327px"></div>

  <div class="contact" style="top:164px">
    <svg viewBox="0 0 20 20" aria-hidden="true"><path fill="#3b4526" d="M2 7c0-2 4-3 8-3s8 1 8 3v2h-4V7.5c-1-.4-2.5-.6-4-.6s-3 .2-4 .6V9H2z M5 10h10l2 6H3z"/><circle cx="10" cy="13" r="1.8" fill="#a8b262"/></svg>
    <span>(555) 014-2837</span>
  </div>
  <div class="contact" style="top:229px">
    <svg viewBox="0 0 20 20" aria-hidden="true" fill="none" stroke="#3b4526" stroke-width="1.3"><circle cx="10" cy="10" r="8"/><ellipse cx="10" cy="10" rx="3.5" ry="8"/><path d="M2 10h16M3.5 6h13M3.5 14h13"/></svg>
    <span>daniel@clearpathmoneycoach.com</span>
  </div>
  <div class="contact" style="top:293px">
    <svg viewBox="0 0 20 20" aria-hidden="true"><rect x="2" y="5" width="16" height="11" fill="#3b4526"/><path d="M2 5l8 6 8-6" fill="none" stroke="#a8b262" stroke-width="1.3"/></svg>
    <span>www.clearpathmoneycoach.com</span>
  </div>
</section>

<section class="card card--back">
  <div class="brand">
    <span class="brand__dot"></span>
    <span class="brand__name">CLEARPATH<br>MONEY COACHING</span>
  </div>
  <div class="pitch">
    <p class="pitch__lead">Struggling with your finances?</p>
    <p>Learn to become <b>debt free</b></p>
    <p>Discover <b>the power of cash</b></p>
    <p><b>Control your money</b> instead of it controlling you</p>
    <p class="pitch__close">Let us help you achieve a new level of financial freedom!</p>
  </div>
  <div class="back__band"></div>
</section>

</body>
</html>
```